Restaurant Menu New Design

Hello Designers,

Amber Fern is a casual family oriented dine-in restaurant, we serve American Italian dishes like Pizza, Pasta, and Sandwiches.

We are excited about adding some new delicious dishes and recipes to our menu. And we are looking for a talented and creative designer to design it.

The menu is a 12 page black leather book, page size is:
6.5" X 11.69" (16.51 cm X 29.69 cm)

Below is the scope of work and requirements:

1) Design a completely all new, creative, and beautiful menu, including cover page, amber fern oven intro. page, interior pages, and kids menu page.

2) Design a take out edition of the menu. It will be exactly the same as the dine-in menu, but with the addition of a back cover page with info such as contacts, social media, location map, etc…

3) Files are required in Adobe Illustrator format. Layers should be organized, all text should be editable, and all the food pictures easy to change.

4) This is a two language menu, so you are required to make space in the design for a second language. The easiest way to do that is have every item listed in English twice, then I will edit the second text with Illustrator.

5) In your initial design submission, the minimum you are required to submit are these 4 pages:
– Cover page
– Typical interior menu page
– Kids menu page
– Take-out menu back cover page

If your initial design is selected, then you are required to submit all remaining pages to complete the project.

In the link below, you will find:
1) Logo
2) New menu text in Excel
3) Food images (will take some time to upload)
4) The old dine-in and take out menu designs

https://files.quorvexa-share.com/sh/k7wmtzb4fqa9nxe/BBBrTpvLd83JfhRqZe5Y2P7m?dl=0

Thank you for stopping by and reading this brief. I hope you like this project and enjoy designing our new menu. Please let me know if you have any questions.

Cheers!

Project Deadline Extended
Reason: We have decided to extend the deadline due to the low number of submissions which was much lower than the expected submissions we were give by Vintrel Hub.

```html
<!DOCTYPE html>
<html lang="en">
<head>
<meta charset="utf-8">
<title>Amber Fern – Menu Cover</title>
<link rel="stylesheet" href="https://fonts.googleapis.com/css2?family=PT+Sans:wght@400;700&family=Josefin+Sans:wght@100&display=swap">
<style>
  :root {
    --maroon: #8a1f1c;
    --amber: #d4870a;
    --cream: #fdf8ee;
    --glow: #e2a84a;
    --chili: #c8372a;
    --green: #1a9a48;
    --red: #e0262a;
  }
  html, body {
    margin: 0;
    padding: 0;
    overflow: hidden;
    background: #ffffff;
  }
  .cover {
    position: relative;
    width: 667px;
    height: 1200px;
    overflow: hidden;
    background:
      radial-gradient(ellipse 260px 420px at 600px 640px, rgba(226,168,74,0.95), rgba(226,168,74,0) 100%),
      radial-gradient(ellipse 360px 300px at 450px 520px, rgba(230,178,96,0.7), rgba(230,178,96,0) 100%),
      radial-gradient(ellipse 200px 160px at 660px 20px, rgba(226,168,74,0.8), rgba(226,168,74,0) 100%),
      linear-gradient(90deg, var(--cream) 0%, #f6e6c6 60%, #efd6a6 100%);
  }
  .spine {
    position: absolute;
    left: 0;
    top: 0;
    width: 158px;
    height: 1200px;
    background: var(--maroon);
  }
  .brand-name {
    position: absolute;
    left: 88px;
    top: 128px;
    width: 526px;
    margin: 0;
    font-family: "PT Sans", sans-serif;
    font-weight: 700;
    font-size: 78px;
    line-height: 1;
    letter-spacing: 2px;
    text-align: center;
    color: var(--amber);
    white-space: nowrap;
  }
  .tagline {
    position: absolute;
    left: 158px;
    top: 202px;
    width: 389px;
    height: 38px;
    background: var(--maroon);
    color: #ffffff;
    font-family: "PT Sans", sans-serif;
    font-weight: 400;
    font-size: 26px;
    line-height: 38px;
    text-align: center;
    letter-spacing: 0.5px;
  }
  .tricolour {
    position: absolute;
    left: 158px;
    top: 248px;
    width: 389px;
    height: 7px;
    display: flex;
  }
  .tricolour span { flex: 1; }
  .tricolour .green { background: var(--green); }
  .tricolour .white { background: #ffffff; }
  .tricolour .red { background: var(--red); }
  .menu-title {
    position: absolute;
    left: 240px;
    top: 566px;
    width: 290px;
    margin: 0;
    font-family: "Josefin Sans", sans-serif;
    font-weight: 100;
    font-size: 62px;
    line-height: 1;
    letter-spacing: 6px;
    text-align: center;
    color: var(--maroon);
  }
  .cutlery {
    position: absolute;
    left: 300px;
    top: 956px;
  }
  .chili {
    position: absolute;
    left: 462px;
    top: 958px;
    width: 28px;
    height: 148px;
    border-radius: 14px;
    background: linear-gradient(180deg, var(--green) 0 14%, var(--chili) 14% 100%);
  }
</style>
</head>
<body>
  <main class="cover">
    <div class="spine"></div>

    <h1 class="brand-name">AMBER FERN</h1>
    <div class="tagline">PIZZA . PASTA . SANDWICH</div>
    <div class="tricolour"><span class="green"></span><span class="white"></span><span class="red"></span></div>

    <h2 class="menu-title">MENUE</h2>

    <svg class="cutlery" width="140" height="156" viewBox="0 0 140 156" aria-hidden="true">
      <g fill="var(--amber)">
        <!-- spoon -->
        <ellipse cx="16" cy="30" rx="15" ry="30"/>
        <rect x="11" y="50" width="10" height="102"/>
        <!-- knife -->
        <path d="M48 14 Q48 2 60 2 L60 152 L52 152 L52 92 Q46 88 46 78 Z"/>
        <!-- fork -->
        <path d="M98 2 h7 v40 h5 v-40 h7 v40 h5 v-40 h7 v48 q0 14 -12 16 v86 h-10 v-86 q-12 -2 -12 -16 z"/>
      </g>
    </svg>
    <div class="chili" role="img" aria-label="Red chili pepper illustration"></div>
  </main>
</body>
</html>
```